Renewable energy company needs modern memorable marketing brochure

We have an 8 page marketing brochure which was created in house. This needs to be revamped and modernised to stand out from our competitors in Australia, Chile and the UK. The brochure should depict us as a professional and dynamic company and instil confidence in prospective clients that we do a professional job. Once the design is finalised we will need a country specific document in the correct language i.e. Spanish for Chile. We are happy to pay for these iterations. We have a company logo which we would like incorporated into the brochure and the colours from the logo utilised where appropriate in the overall design. I have uploaded our existing brochure for an example of the content that the brochure needs to have and can upload the images separately if they are needed. Images in the brochure need to be copyright free and we have lots of photos in-house. I have added all the images from the last brochure and also the text in Indesign so it can be copied easily if needed.

Target Market(s)

landowners and companies

Industry/Entity Type

It Company

Requirements
Must have
• A clean modern look with some colours taken from the logo colour. Be easy to print in various countries.

```html
<!DOCTYPE html>
<html lang="en">
<head>
<meta charset="utf-8">
<title>Recent Case Studies – Solvane Power Brochure Spread</title>
<link href="https://fonts.googleapis.com/css2?family=Ubuntu:wght@400;500;700&display=swap" rel="stylesheet">
<style>
  :root {
    --teal: #1aa592;
    --ink: #3d3d3d;
    --body: #4a4a4a;
    --header-bg: #efefef;
    --page: #ffffff;
    --backdrop: #e4e7e8;
    --panel-blue: #2f3d6b;
  }
  * { box-sizing: border-box; margin: 0; padding: 0; }
  html, body {
    width: 1200px; height: 1200px; overflow: hidden;
    background: var(--backdrop);
    font-family: "Ubuntu", sans-serif;
    color: var(--body);
  }
  .spread {
    position: absolute; left: 40px; top: 206px;
    width: 918px; height: 645px;
    transform: scale(1.22); transform-origin: top left;
    background: var(--page);
    box-shadow: 0 4px 14px rgba(0,0,0,.12);
    overflow: hidden;
  }
  .masthead {
    position: absolute; left: 0; top: 0; width: 918px; height: 67px;
    background: var(--header-bg);
  }
  .masthead-rule {
    position: absolute; left: 0; top: 67px; width: 918px; height: 6px;
    background: var(--teal);
  }
  .page-title {
    position: absolute; left: 16px; top: 16px;
    font-size: 25px; font-weight: 700; color: var(--ink); letter-spacing: -.3px;
  }
  .page-title .accent { color: var(--teal); font-weight: 400; }
  .brand {
    position: absolute; left: 775px; top: 11px;
    display: flex; align-items: center; gap: 10px;
  }
  .brand-mark { width: 46px; height: 46px; }
  .brand-name {
    font-size: 13.5px; font-weight: 400; line-height: 14px; color: var(--ink);
    letter-spacing: .3px;
  }
  .intro {
    position: absolute; left: 19px; top: 92px; width: 424px;
    font-size: 10.2px; line-height: 15.4px; text-align: justify;
  }
  .photo { position: absolute; }
  .photo-ashbrook { left: 19px; top: 180px; width: 188px; height: 205px;
    background: linear-gradient(180deg, #e6ecef 0%, #b9cbd8 22%, #3d5b86 50%, #7f9bbb 70%, #5e7d3a 100%); }
  .photo-kelmere { left: 19px; top: 420px; width: 188px; height: 205px;
    background: linear-gradient(180deg, #dcdcd4 0%, #a9a27a 25%, #7a8a4c 42%, var(--panel-blue) 58%, #4a5a35 74%, #3f5a26 100%); }
  .photo-hollin { left: 482px; top: 94px; width: 185px; height: 205px;
    background: linear-gradient(180deg, #3b4a25 0%, #7e8b5f 25%, #c9cfd2 40%, #8d9bb0 50%, #c9bd94 66%, #9aa066 100%); }
  .photo-thornby { left: 482px; top: 334px; width: 185px; height: 205px;
    background: linear-gradient(180deg, #dfe2e1 0%, #d6d8c8 38%, #b4b957 46%, #7d8f64 55%, #93a55a 75%, #5b4a3a 94%, #6f675b 100%); }
  .photo-aerial { left: 462px; top: 515px; width: 456px; height: 130px;
    background: linear-gradient(180deg, rgba(255,255,255,0) 0%, rgba(168,176,150,.7) 30%, #6e7a8f 55%, var(--panel-blue) 80%, #5b6a3c 100%); }
  .case { position: absolute; width: 225px; }
  .case-ashbrook { left: 222px; top: 179px; }
  .case-kelmere { left: 222px; top: 418px; }
  .case-hollin { left: 682px; top: 93px; }
  .case-thornby { left: 682px; top: 333px; }
  .case-name { font-size: 12.8px; font-weight: 500; color: var(--teal); line-height: 15px; }
  .case-spec { font-size: 9.6px; line-height: 13px; margin-bottom: 15px; }
  .case-label { font-size: 9.8px; font-weight: 500; color: var(--ink); margin-bottom: 4px; }
  .highlights { list-style: none; }
  .highlights li {
    position: relative; padding-left: 10px; font-size: 9.6px; line-height: 12.8px; margin-bottom: 6px;
  }
  .highlights li::before {
    content: ""; position: absolute; left: 0; top: 3.5px;
    width: 6px; height: 6px; border: 1.3px solid var(--teal); border-radius: 50%;
  }
</style>
</head>
<body>
  <article class="spread">
    <header class="masthead">
      <h1 class="page-title">RECENT CASE <span class="accent">STUDIES</span></h1>
      <div class="brand">
        <svg class="brand-mark" viewBox="0 0 46 46" aria-hidden="true">
          <circle cx="23" cy="23" r="20" fill="var(--teal)"/>
        </svg>
        <div class="brand-name">SOLVANE<br>POWER</div>
      </div>
    </header>
    <div class="masthead-rule"></div>

    <p class="intro">With experience of developing over 100 MWp, Solvane Power's portfolio is one of the largest in the UK. Solvane Power is partnered with two of the largest and most experienced intergrated solar companies in the world and therefore has access to construction finance and the latest in solar technology</p>

    <div class="photo photo-ashbrook" role="img" aria-label="Photo: rows of solar panels reflecting a cloudy sky beside a grass verge"></div>
    <section class="case case-ashbrook">
      <h2 class="case-name">Ashbrook Solar Farm</h2>
      <p class="case-spec">48 MWp, 76 Hectares, Ashbrook, UK</p>
      <h3 class="case-label">Highligts :</h3>
      <ul class="highlights">
        <li>Development approval granted in September 2015, construction beginning shortly</li>
        <li>Will be one of the largest and most technologically advanced solar farms in the UK</li>
        <li>Has development approval to install battery storage</li>
        <li>A local agricultural college and University will use the site for research</li>
      </ul>
    </section>

    <div class="photo photo-kelmere" role="img" aria-label="Photo: aerial view of a solar farm among fields and woodland"></div>
    <section class="case case-kelmere">
      <h2 class="case-name">Kelmere Solar Farm</h2>
      <p class="case-spec">11.6 MWp, 27 Hectares, Kelmere Green, UK</p>
      <h3 class="case-label">Highligts :</h3>
      <ul class="highlights">
        <li>Commissioned March 2015</li>
        <li>One of the UK's first solar farms to allow community to invest</li>
        <li>Diversification of income for landowner along with a long term maintenance contract</li>
        <li>Landowner offers 'solar farm tours'</li>
      </ul>
    </section>

    <div class="photo photo-hollin" role="img" aria-label="Photo: fruit farm rows under a tree with solar panels in the distance"></div>
    <section class="case case-hollin">
      <h2 class="case-name">Hollin Vale Solar Farm</h2>
      <p class="case-spec">8.7 MWp, 22 Hectares, Hollin Vale, UK</p>
      <h3 class="case-label">Highligts :</h3>
      <ul class="highlights">
        <li>Commissioned March 2015</li>
        <li>One of the UK's first solar farms to allow community to invest</li>
        <li>Integrated within a fruit farm</li>
        <li>Has development approval to install battery storage</li>
      </ul>
    </section>

    <div class="photo photo-aerial" role="img" aria-label="Photo: hazy aerial view of a large solar farm in the countryside"></div>
    <div class="photo photo-thornby" role="img" aria-label="Photo: grassy field beside a railway line with solar panels and yellow fields beyond"></div>
    <section class="case case-thornby">
      <h2 class="case-name">Thornby Solar Farm</h2>
      <p class="case-spec">26.1 MWp, 36 Hectares, Thornby Cross, UK</p>
      <h3 class="case-label">Highligts :</h3>
      <ul class="highlights">
        <li>Development approval granted in October 2015, construction beginning shortly</li>
        <li>Will be one of the largest and most technologically advanced solar farms in the UK</li>
        <li>Diversification of income for landowner along with a long term maintenance contract</li>
        <li>Has development approval to install battery storage</li>
      </ul>
    </section>
  </article>
</body>
</html>
```